BRIGHTWAVE PARTNERS NAMECARD

Need to design a name card with an existing logo.

As we are professional corporate services provider our name card has to project a professional image.
Should be corporate, simple & professional.

Our corporate color is maroon red but not too dull.

Please refer to our website at www.brightwavepartners.com.sg

Would attach our logo herewith.

Front surface of namecard details:
BRIGHTWAVE PARTNERS PTE LTD
Registration No. 208731945K

Lowe Hui Ting CA (Singapore)
Director

Tel +65 6481 2957
Mobile +65 9172 3806
lowe@brightwavepartners.com.sg
www.brightwavepartners.com.sg

47 Palmer Lane
#07-14 Harbourlight Plaza
Singapore 274153

Back of namecard:-
OUR CORE SERVICES
Incorporation services
Corporate Secretarial Services
Accountancy service
Goods & Services Taxation
Corporate & Personal Taxation
Financial Reporting
Payroll Administration

AFFILIATES:
TRIVANTA CORPORATE SERVICES PTE LTD
BRIGHTWAVEREGISTRYPTE LTD
ORR MANAGEMENT SERVICES PTE LTD
DW LIM AND COMPANY PTE LTD
LEDGERWISE ACADEMY

```html
<!DOCTYPE html>
<html lang="en">
<head>
<meta charset="utf-8">
<title>Brightwave Partners Namecard</title>
<link rel="stylesheet" href="https://fonts.googleapis.com/css2?family=PT+Sans:wght@400;700&display=swap">
<style>
  :root {
    --backdrop: #9c9ca1;
    --brand-red: #d2243a;
    --brand-red-light: #dc4a5a;
    --paper: #ffffff;
    --paper-shade: #eeeeee;
    --ink-light: #ffffff;
  }
  * { box-sizing: border-box; margin: 0; padding: 0; }
  html, body {
    width: 1200px; height: 863px; overflow: hidden;
    background: var(--backdrop);
    font-family: "PT Sans", Arial, sans-serif;
  }
  .canvas { position: relative; width: 1200px; height: 863px; }
  .card {
    position: absolute; width: 560px; height: 336px;
    background: linear-gradient(135deg, var(--brand-red), var(--brand-red-light));
    box-shadow: 0 8px 18px rgba(0,0,0,0.28);
    overflow: hidden; color: var(--ink-light);
  }
  .wordmark {
    color: var(--brand-red); font-weight: 700;
    letter-spacing: 0.02em; line-height: 0.95; text-transform: uppercase;
  }

  /* Back of card */
  .card-back { left: 580px; top: 60px; }
  .card-back .header-band {
    height: 80px; background: linear-gradient(180deg, var(--paper), var(--paper-shade));
    display: flex; justify-content: flex-end; align-items: center; padding-right: 34px;
  }
  .card-back .wordmark { font-size: 27px; text-align: center; }
  .card-back .content { display: flex; padding: 16px 24px 0; gap: 18px; }
  .card-back .column { flex: 1; }
  .card-back .services { text-align: right; }
  .card-back h2 {
    font-size: 12px; font-weight: 400; letter-spacing: 0.03em; margin-bottom: 10px;
  }
  .card-back ul { list-style: none; font-size: 12.5px; line-height: 1.55; }
  .card-back .affiliates ul { font-size: 11.5px; }

  /* Front of card */
  .card-front { left: 60px; top: 450px; display: flex; }
  .card-front .logo-panel {
    width: 205px; height: 100%;
    background: linear-gradient(180deg, var(--paper), var(--paper-shade));
    display: flex; align-items: center; justify-content: center;
  }
  .card-front .wordmark { font-size: 29px; text-align: center; }
  .card-front .details { padding: 30px 0 0 26px; }
  .card-front .name { font-size: 21px; font-weight: 400; }
  .card-front .role { font-size: 12.5px; margin-top: 2px; }
  .card-front .contact { margin-top: 30px; font-size: 13.5px; line-height: 1.45; }
  .card-front .address { margin-top: 18px; font-size: 13.5px; line-height: 1.45; }
  .card-front .registration { margin-top: 8px; font-size: 13.5px; }
</style>
</head>
<body>
<main class="canvas">

  <section class="card card-back" aria-label="Back of namecard">
    <div class="header-band">
      <div class="wordmark">Brightwave<br>Partners</div>
    </div>
    <div class="content">
      <div class="column services">
        <h2>OUR CORE SERVICES</h2>
        <ul>
          <li>Incorporation services</li>
          <li>Corporate Secretarial Services</li>
          <li>Accountancy service</li>
          <li>Goods &amp; Services Taxation</li>
          <li>Corporate &amp; Personal Taxation</li>
          <li>Financial Reporting</li>
          <li>Payroll Administration</li>
        </ul>
      </div>
      <div class="column affiliates">
        <h2>AFFILIATES</h2>
        <ul>
          <li>TRIVANTA CORPORATE SERVICES PTE LTD</li>
          <li>BRIGHTWAVEREGISTRYPTE LTD</li>
          <li>ORR MANAGEMENT SERVICES PTE LTD</li>
          <li>DW LIM AND COMPANY PTE LTD</li>
          <li>LEDGERWISE ACADEMY</li>
        </ul>
      </div>
    </div>
  </section>

  <section class="card card-front" aria-label="Front of namecard">
    <div class="logo-panel">
      <div class="wordmark">Brightwave<br>Partners</div>
    </div>
    <div class="details">
      <p class="name">Lowe Hui Ting CA (Singapore)</p>
      <p class="role">Director</p>
      <p class="contact">
        Tel +65 6481 2957<br>
        Mobile +65 9172 3806<br>
        lowe@brightwavepartners.com.sg<br>
        www.brightwavepartners.com.sg
      </p>
      <p class="address">
        47 Palmer Lane, #07-14 Harbourlight Plaza<br>
        Singapore 274153
      </p>
      <p class="registration">Registration No. 208731945K</p>
    </div>
  </section>

</main>
</body>
</html>
```